Stationery Design Project

We need letterhead and business cards designed for our consulting firm. Color scheme, mostly deep blue (see logo). We are a commercial consulting work out firm, nationwide (large loans, $10MM and up). Visit our website for more info.
Updates

Project Deadline Extended
Reason: Meeting tomorrow morning to make final final decision. Would like this project to stay open to be able to provide feed back and receive final edits and approve. Thank you!!!

Target Market(s)

High end investors

Industry/Entity Type

Business

Requirements
Must have
• Letterhead must have the logo and the address

4719 Harlow Court, Suite 210, San Diego, CA 92108
Nice to have
• It would be nice to incorporate a watermark of all or some portion of the logo on the letterhead, or at least for the 2nd sheets.

Maybe our phone number: 858.555.0172
and/or webiste: www.tallpinecapital-example.com
Should not have
• Target users and audience of this will be men so, frilly or whimsical type designs are not preferred.

```html
<!DOCTYPE html>
<html lang="en">
<head>
<meta charset="utf-8">
<title>Tallpine Capital – Stationery</title>
<link rel="stylesheet" href="https://fonts.googleapis.com/css2?family=Arimo:wght@400;700&family=Cinzel:wght@400&display=swap">
<style>
  :root {
    --stage-top: #efefef;
    --stage-bottom: #8a8a8a;
    --card-dark: #333333;
    --ink-black: #000000;
    --stripe-light: #9a9a9a;
    --stripe-dark: #555555;
    --brand-blue: #3aa0dc;
    --brand-cyan: #6ad6f0;
    --brand-deep: #2b8ccc;
    --logo-grey: #7c838c;
    --watermark: #d7dbe0;
    --paper: #fbfbfb;
    --paper-edge: #9cc8ea;
    --white: #ffffff;
    --label: #111111;
  }
  html, body { margin: 0; padding: 0; overflow: hidden; }
  .canvas {
    position: relative; width: 777px; height: 1200px; overflow: hidden;
    background: linear-gradient(160deg, var(--stage-top) 0%, #cfcfcf 45%, var(--stage-bottom) 100%);
    font-family: "Arimo", Arial, sans-serif;
  }
  .abs { position: absolute; }
  .section-label { font-size: 16px; color: var(--label); letter-spacing: 0.2px; }
  .brand-name {
    font-family: "Cinzel", Georgia, serif; font-weight: 400; white-space: nowrap;
    display: flex; align-items: center; gap: 10px;
  }
  .brand-mark { display: inline-block; flex-shrink: 0; background: var(--brand-blue); }
  .stripe-fill { background: linear-gradient(135deg, var(--stripe-light), var(--stripe-dark)); }

  .hero-brand { left: 134px; top: 61px; width: 300px; height: 134px; justify-content: center; font-size: 32px; color: var(--logo-grey); }
  .hero-brand .brand-mark { width: 22px; height: 22px; }

  .card { width: 248px; height: 141px; background: var(--card-dark); overflow: hidden; }
  .card-front { left: 487px; top: 65px; }
  .card-back { left: 375px; top: 217px; border: 1px solid #555; }
  .card-band { left: 0; top: 65px; width: 226px; height: 44px; background: var(--ink-black); }
  .card-front .brand-name { left: 0; top: 65px; width: 226px; height: 44px; justify-content: center; gap: 8px; font-size: 18px; color: #b9bec4; }
  .card-front .brand-mark { width: 12px; height: 12px; }
  .card-back .brand-name { right: 6px; top: 4px; font-family: "Arimo", Arial, sans-serif; font-weight: 700; font-size: 12px; color: var(--brand-blue); }

  .contact { font-size: 8px; line-height: 10.5px; color: var(--white); white-space: nowrap; }
  .contact .indent { padding-left: 41px; }
  .card-contact { left: 0; top: 26px; width: 184px; height: 83px; background: rgba(58,160,220,0.92); box-sizing: border-box; padding: 5px 7px; }

  .letterhead { left: 86px; top: 386px; width: 599px; height: 776px; background: var(--paper); border: 1px solid var(--paper-edge); box-sizing: border-box; }
  .lh-column { left: 0; top: 0; width: 78px; height: 100%; }
  .lh-logo-box { left: 15px; top: 5px; width: 216px; height: 82px; background: var(--ink-black); box-sizing: border-box; padding-left: 12px; justify-content: flex-start; gap: 8px; font-size: 15px; color: #b9bec4; }
  .lh-logo-box .brand-mark { width: 11px; height: 11px; }
  .lh-contact { left: 215px; top: 26px; width: 190px; height: 83px; background: var(--brand-cyan); box-sizing: border-box; padding: 5px 8px; font-weight: 700; overflow: hidden; }
  .lh-contact-edge { left: 0; top: 0; width: 32px; height: 100%; background: var(--brand-deep); opacity: 0.8; }
  .lh-contact-text { position: relative; }
  .lh-watermark { left: 238px; top: 352px; width: 307px; height: 138px; justify-content: center; font-size: 28px; color: var(--watermark); }
  .lh-watermark .brand-mark { width: 18px; height: 18px; background: var(--watermark); }
</style>
</head>
<body>
<main class="canvas">
  <div class="abs brand-name hero-brand"><span class="brand-mark"></span>Tallpine Capital</div>

  <div class="abs section-label" style="left:486px; top:42px;">BUSINESS CARD</div>

  <section class="abs card card-front">
    <div class="abs stripe-fill" role="img" aria-label="Diagonal grey stripe pattern" style="left:15px; top:8px; width:166px; height:57px;"></div>
    <div class="abs stripe-fill" role="img" aria-label="Diagonal grey stripe pattern" style="left:159px; top:109px; width:89px; height:32px;"></div>
    <div class="abs card-band"></div>
    <div class="abs brand-name"><span class="brand-mark"></span>Tallpine Capital</div>
  </section>

  <section class="abs card card-back">
    <div class="abs stripe-fill" role="img" aria-label="Diagonal grey stripe pattern" style="left:0; top:0; width:88px; height:24px;"></div>
    <div class="abs" style="left:29px; top:57px; width:217px; height:83px; background:var(--ink-black);"></div>
    <div class="abs brand-name">Tallpine Capital</div>
    <div class="abs contact card-contact">
      <div>Address : 4719 Harlow Court,</div>
      <div class="indent">Suite 210,</div>
      <div class="indent">San Diego,</div>
      <div class="indent">CA 92108</div>
      <div>phone number: 858.555.0172</div>
      <div>Email: info@tallpinecapital-example.com</div>
      <div>webiste: www.tallpinecapital-example.com</div>
    </div>
  </section>

  <div class="abs section-label" style="left:93px; top:337px;">LETTER HEAD</div>

  <section class="abs letterhead">
    <div class="abs lh-column stripe-fill" role="img" aria-label="Diagonal grey stripe pattern down the left margin"></div>
    <div class="abs brand-name lh-logo-box"><span class="brand-mark"></span>Tallpine Capital</div>
    <div class="abs contact lh-contact">
      <div class="abs lh-contact-edge"></div>
      <div class="lh-contact-text">
        <div>Address : 4719 Harlow Court,</div>
        <div class="indent">Suite 210,</div>
        <div class="indent">San Diego,</div>
        <div class="indent">CA 92108</div>
        <div>phone number: 858.555.0172</div>
        <div>Email: info@tallpinecapital-example.com</div>
        <div>webiste: www.tallpinecapital-example.com</div>
      </div>
    </div>
    <div class="abs brand-name lh-watermark"><span class="brand-mark"></span>Tallpine Capital</div>
  </section>
</main>
</body>
</html>
```